Hey,
My name is Tomas Vellanegra and I'm starting a PhD in Physics next year. I want to a bit more than just research on my own. I want to bring some public involvement to it.
"Zeta Quarks" is website/wordpress/blog. It is a way to bring physics to the general public without losing the math or the physics essence - This is a place to share fun and interesting findings that PhD students, Professors, High school students and basically everyone else that loves and wants to know a bit more about nature. The idea is to put real science to debate in a open non-judgmental way in prol of knowledge and discovery. "Everybody" is welcome to post relevant things such as experiments made at home as well as their latest discovery in their super high tech £100M lab.
The first step of the project is to develop a BLOG (Wordpress) - the domain is already register "zetaquarks.org and zetaquarks.com" that could host that initial debate and posts.
Think http://lensmoravia.org/ ; http://www.wavecellar.org/; https://www.youtube.com/user/ninetyglyphs; https://www.youtube.com/user/secondquanta as a guidelines...
http://trevilo.bvx.com.br/
I would enjoy touches of watercolour design here and there.
I also like pastel colours. But remember, I am a scientist and not at all designer. I'll trust the artists to create and show me what they are up to.
UPDATE: Just so you guys know. I want to do a Website in form of a Blog. I want to easily post and upload videos and articles related to Physics.
I'm more familiar with Wordpress but if you say that any other platform does the job better and I can still maintain the domain zetaquarks.org lets do it!
Update number 2: I will respond every designer asap. I will however do that between 9:00am and 14:00 pm Brasilia/Brazil Time.
So please don't get upset or take it personal if you don't get a feedback right away, specially if it is 02:00 a.m my time, ok ?! : - )
Thanks Guys and good work!
For all designers that just want to do logos please post them in: Manage Project | Zeta Quarks - Logo Design Project
We will continue from there!
Target Market(s)
Everyone that likes physics, no matter if you are a Nobel Laureate or a single mother that likes physics.
Industry/Entity Type
Artists
Font styles to use
Other font styles liked:
- I like Calibri, Helvetica, Verdana, Univers and Tahoma for body text, Sometimes I use Arial. Cambria and Georgia for headings
Requirements
Must have
- I'm open minded! But I like thinks to be simple!
Nice to have
- The way you going to put "Zeta Quarks" is completely up to you. I usually like it simple but. Show me what you got and I'll give you feedback if I like it or not! Just remember to keep it clean and user friendly.
Should not have
- Just try beautiful and functional designs. I usually don't like super old style fonts like Times New Roman and very elaborate things that are hard to read.

```html
<!DOCTYPE html>
<html lang="en">
<head>
<meta charset="utf-8">
<title>Zeta Quarks</title>
<link href="https://fonts.googleapis.com/css2?family=Ubuntu:wght@300;400;500;700&family=Open+Sans:ital,wght@0,400;0,600;0,700;1,400;1,700&display=swap" rel="stylesheet">
<style>
:root{
  --bg:#eeeeec;
  --panel:#f7f7f6;
  --line:#dcdcdc;
  --red:#ef4f5b;
  --band:#f05a63;
  --ink:#444444;
  --muted:#666666;
  --blue:#1f6fae;
  --navy:#215d93;
  --yellow:#fcd13a;
  --orange:#f28b22;
  --green:#58a92a;
  --dark:#2b2b2b;
  --darker:#1b1b1b;
}
*{box-sizing:border-box;margin:0;padding:0}
html,body{width:703px;height:1200px;overflow:hidden}
body{background:var(--bg);font-family:"Open Sans",Arial,sans-serif;color:var(--ink);position:relative}
.abs{position:absolute}
.topline{left:0;top:0;width:703px;height:3px;background:#555}
.logo{left:62px;top:10px;font-family:"Ubuntu",sans-serif;font-weight:500;font-size:30px;color:var(--red);letter-spacing:-0.5px}
.contact{left:518px;top:32px;display:flex;gap:6px;align-items:center}
.contact .phone{font-family:"Ubuntu",sans-serif;font-weight:500;font-size:12px;color:var(--navy);line-height:1}
.contact .mail{font-size:7.5px;color:var(--orange);text-align:right}
.band{left:0;top:82px;width:703px;height:234px;background:linear-gradient(180deg,#f2636b,#ec4f59)}
.nav{left:60px;top:68px;width:584px;height:26px;background:#fafafa;border:1px solid #d8d8d8;border-radius:5px;display:flex;z-index:2;box-shadow:0 1px 2px rgba(0,0,0,.15)}
.nav a{font-size:7.5px;color:#333;text-decoration:none;display:flex;align-items:center;justify-content:center;border-right:1px solid #ddd;text-transform:uppercase}
.nav a:last-child{border-right:0}
.nav a.active{background:#5b5b5b;color:#fff;margin-top:-6px;border-radius:4px 4px 0 0;border:0}
.hero{left:58px;top:106px;width:409px;height:199px;background:linear-gradient(180deg,#fff,#efefef);border-radius:6px;box-shadow:0 2px 4px rgba(0,0,0,.2);overflow:hidden}
.hero .photo{position:absolute;left:18px;top:4px;width:180px;height:195px;background:linear-gradient(160deg,#d7dde6,#9fb0c4 55%,#c9d3dd);border-radius:4px}
.hero h2{position:absolute;left:197px;top:21px;font-family:"Ubuntu",sans-serif;font-weight:500;font-size:14px;color:var(--navy)}
.hero p{position:absolute;left:196px;top:40px;width:205px;font-size:8.5px;line-height:1.25;color:#333}
.hero p em{font-style:normal;font-family:"Ubuntu",sans-serif;font-weight:300;font-size:15px;color:var(--red);line-height:1.1}
.hero ul{position:absolute;left:226px;top:104px;list-style:none;font-size:7.5px;line-height:11.6px;color:#333}
.hero li::before{content:"";display:inline-block;width:5px;height:5px;background:var(--blue);transform:rotate(45deg);margin-right:6px}
.dots{position:absolute;left:360px;top:184px;display:flex;gap:4px}
.dots span{width:7px;height:7px;border-radius:50%;border:1px solid #999;background:#fff}
.dots span:first-child{background:#111;border-color:#111}
.ask{left:481px;top:108px;width:156px;height:198px;background:var(--yellow);border:2px solid #fff0a8;border-radius:5px;text-align:center;padding-top:10px}
.ask h3{font-family:"Ubuntu",sans-serif;font-weight:500;font-size:10.5px;color:#fff;line-height:13px}
.ask p{font-size:10px;color:#fff;line-height:13px}
.ask p b{font-style:italic}
.ask .area{position:absolute;left:7px;top:88px;width:142px;height:34px;background:#fff;border-radius:8px}
.ask .field{position:absolute;left:9px;top:135px;width:138px;height:17px;background:#fff;border-radius:9px;border:1px solid #e8c24a}
.ask .btn{position:absolute;left:45px;top:165px;width:66px;height:19px;border-radius:10px;background:linear-gradient(#3b8de0,#1e5fb2);color:#fff;font-size:9px;font-weight:600;line-height:19px}
.sec-head{left:66px;top:336px;display:flex;align-items:center;gap:6px;font-family:"Ubuntu",sans-serif;font-weight:500;font-size:13px;color:#444}
.rss{width:16px;height:16px;border-radius:4px;background:var(--orange)}
.post{left:30px;width:434px}
.post .rule{position:absolute;left:36px;top:-6px;width:398px;border-top:2px dotted #c8c8c8}
.post h4{position:absolute;left:38px;top:0;font-family:"Ubuntu",sans-serif;font-weight:500;font-size:10.5px;color:var(--red)}
.date{position:absolute;left:0;top:2px;width:30px;height:44px;background:var(--yellow);border-radius:3px;color:#fff;text-align:center;font-family:"Ubuntu",sans-serif;line-height:1}
.date b{display:block;font-size:8px;font-weight:400;margin-top:4px}
.date i{display:block;font-style:normal;font-size:11px;font-weight:700}
.date span{display:block;font-size:7px;margin-top:1px}
.post .img{position:absolute;left:36px;top:14px;width:128px;height:86px;border:2px solid #fff;box-shadow:0 1px 3px rgba(0,0,0,.3)}
.post .text{position:absolute;left:176px;top:14px;width:240px;font-size:6.3px;line-height:10.5px;color:#555}
.post .text strong{font-style:italic;font-weight:700;color:#444}
.post .text p{margin-bottom:5px}
.post .more{position:absolute;left:176px;font-size:6.5px;font-weight:700;color:#333}
.post .share{position:absolute;right:0;display:flex;align-items:center;gap:2px;font-size:6.5px;color:#777}
.share i{display:inline-block;width:9px;height:9px;border:1px solid #999;background:#fff}
.share i:last-child{background:#888}
.box{background:var(--panel);border:1px solid #e3e3e3;border-radius:6px;box-shadow:0 1px 2px rgba(0,0,0,.06)}
.connect{left:482px;top:336px;width:154px;height:58px}
.connect h5{position:absolute;left:11px;top:8px;font-family:"Ubuntu",sans-serif;font-weight:500;font-size:10.5px;color:var(--red)}
.connect .soc{position:absolute;top:28px;width:24px;height:24px;border-radius:50%}
.side-title{position:absolute;left:8px;font-family:"Ubuntu",sans-serif;font-weight:500;font-size:12px;color:var(--blue)}
.helpful{left:482px;top:402px;width:154px;height:190px}
.helpful ul{position:absolute;left:8px;top:31px;width:128px;list-style:none}
.helpful li{font-size:6.8px;height:15.3px;line-height:14px;border-bottom:1px solid #e0e0e0;color:#444}
.helpful li::before{content:"»";color:#999;margin-right:5px}
.access{position:absolute;left:17px;top:162px;width:122px;height:22px;background:var(--green);border-radius:2px;color:#fff;font-size:7.5px;font-weight:700;text-align:center;line-height:22px;box-shadow:0 2px 0 #3c7d19}
.lastest{left:482px;top:604px;width:154px;height:196px}
.lp{position:absolute;left:8px;width:140px}
.lp a{display:block;font-size:6px;font-weight:700;color:var(--navy);text-decoration:underline;line-height:9px}
.lp .thumb{position:absolute;left:0;top:24px;width:39px;height:36px;background:linear-gradient(135deg,#2c3447,#8a5a3a 60%,#3d2b24)}
.lp p{position:absolute;left:46px;top:22px;width:94px;font-size:6.8px;line-height:10px;color:#555}
.tags{left:482px;top:816px;width:154px;height:184px}
.tags .tag-icon{position:absolute;left:11px;top:12px;width:12px;height:12px;background:var(--orange);border-radius:2px}
.tags h5{position:absolute;left:28px;top:12px;font-family:"Ubuntu",sans-serif;font-weight:500;font-size:10px;color:var(--blue)}
.cloud{position:absolute;left:14px;top:32px;width:134px;font-family:"Ubuntu",sans-serif;font-weight:300;color:#333;line-height:1}
.cloud div{margin-bottom:5px;white-space:nowrap}
.footer{left:0;top:1014px;width:703px;height:150px;background:var(--dark)}
.fcol{position:absolute;top:20px}
.fcol h6{font-family:"Ubuntu",sans-serif;font-weight:500;font-size:11px;color:#fff;margin-bottom:8px}
.fcol ul{list-style:none}
.fcol li{font-size:7px;color:#bbb;line-height:14px}
.fcol li::before{content:"";display:inline-block;width:4px;height:4px;border-radius:50%;background:#2b8de0;margin-right:7px;vertical-align:middle}
.fcol.addr li::before{display:none}
.map{left:448px;top:1022px;width:190px;height:134px;border:2px solid #fff;background:linear-gradient(135deg,#eee6c8,#f4e8a8 50%,#dfe6ea)}
.bottom{left:0;top:1164px;width:703px;height:36px;background:var(--darker);text-align:center}
.bottom nav{display:flex;justify-content:center;gap:23px;padding-top:7px;font-size:6.5px;color:#ddd;text-transform:uppercase}
.bottom p{font-size:6.5px;color:#ccc;margin-top:8px}
</style>
</head>
<body>
<div class="abs topline"></div>
<div class="abs logo">Zeta Quarks</div>
<div class="abs contact">
  <svg width="22" height="24" viewBox="0 0 22 24" aria-hidden="true"><path d="M6 3c2-1 3 0 4 3l-2 2c1 3 3 5 6 6l2-2c3 1 4 2 3 4-1 3-4 4-7 2C7 16 4 12 3 8 2 5 3 4 6 3z" fill="var(--orange)"/></svg>
  <div><div class="phone">+1-555-014-2270</div><div class="mail">Info@zetaquarks.com</div></div>
</div>

<div class="abs band"></div>
<nav class="abs nav">
  <a style="width:60px">Home</a>
  <a class="active" style="width:102px">Did you know?</a>
  <a style="width:144px">Why choose Zeta Quarks</a>
  <a style="width:120px">60 second lessons</a>
  <a style="width:93px">Recommend</a>
  <a style="width:65px">About</a>
</nav>

<section class="abs hero">
  <div class="photo" role="img" aria-label="Smiling teacher giving a thumbs up beside stacked books, a graduation cap and a diploma"></div>
  <h2>Did You Know?</h2>
  <p>This website provides physics <em>resources for students at School</em> and the public at large.</p>
  <ul>
    <li>Policies &amp; Procedures</li>
    <li>Audit and Verification</li>
    <li>Fees Analysis</li>
    <li>Best Practices</li>
    <li>Accelerating Results</li>
    <li>Pricing Negotiations</li>
  </ul>
  <div class="dots"><span></span><span></span><span></span></div>
</section>

<aside class="abs ask">
  <h3>Ask our experts your<br>Zeta Quarks Questions</h3>
  <p>We might just make it into<br><b>our next “Did You Know?”</b><br>entry</p>
  <div class="area"></div>
  <div class="field"></div>
  <div class="btn">Submit</div>
</aside>

<div class="abs sec-head"><span class="rss"></span>LATEST POSTS</div>

<article class="abs post" style="top:372px">
  <div class="rule" style="top:-7px"></div>
  <div class="date"><b>16</b><i>Dec</i><span>2011</span></div>
  <h4>Why the Sky is Blue explained in ten seconds</h4>
  <div class="img" role="img" aria-label="Teacher writing graphs on a whiteboard" style="background:linear-gradient(120deg,#e8e8e6,#b8c3cf 50%,#6f86a6)"></div>
  <div class="text">
    <p><strong>Workplace Wire Headline News: Find out what's going on in the world of corporate and business communications.</strong> Signal Lines: Learn about using communications to better communicate within your organization, and with others outside your organization. Office Lens: This blog is meant for corporate communications professionals.</p>
    <p>Workplace Wire Headline News: Find out what's going on in the world of corporate and business communications.</p>
  </div>
  <div class="more" style="top:108px">Continue Reading</div>
  <div class="share" style="top:106px">Share This <i></i><i></i><i></i><i></i></div>
</article>

<article class="abs post" style="top:510px">
  <div class="rule"></div>
  <div class="date"><b>16</b><i>Dec</i><span>2011</span></div>
  <h4>Why the Sky is Blue explained in ten seconds</h4>
  <div class="img" role="img" aria-label="Group of colleagues around a laptop" style="background:linear-gradient(120deg,#f2f2f0,#c9c4bd 50%,#3d3f47)"></div>
  <div class="text">
    <p><strong>Workplace Wire Headline News: Find out what's going on in the world of corporate and business communications.</strong> Signal Lines: Learn about using communications to better communicate within your organization, and with others outside your organization. Office Lens: This blog is meant for corporate communications professionals.</p>
    <p>Workplace Wire Headline News: Find out what's going on in the world of corporate and business communications.</p>
  </div>
  <div class="more" style="top:108px">Continue Reading</div>
  <div class="share" style="top:106px">Share This <i></i><i></i><i></i><i></i></div>
</article>

<article class="abs post" style="top:653px">
  <div class="rule"></div>
  <div class="date"><b>16</b><i>Dec</i><span>2011</span></div>
  <h4>Why the Sky is Blue explained in ten seconds</h4>
  <div class="img" role="img" aria-label="Teacher writing graphs on a whiteboard" style="background:linear-gradient(120deg,#e8e8e6,#b8c3cf 50%,#6f86a6)"></div>
  <div class="text">
    <p><strong>Workplace Wire Headline News: Find out what's going on in the world of corporate and business communications.</strong> Signal Lines: Learn about using communications to better communicate within your organization, and with others outside your organization. Office Lens: This blog is meant for corporate communications professionals.</p>
    <p>Workplace Wire Headline News: Find out what's going on in the world of corporate and business communications.</p>
  </div>
  <div class="more" style="top:104px">Continue Reading</div>
  <div class="share" style="top:102px">Share This <i></i><i></i><i></i><i></i></div>
</article>

<article class="abs post" style="top:798px">
  <div class="rule"></div>
  <div class="date"><b>16</b><i>Dec</i><span>2011</span></div>
  <h4>Why the Sky is Blue explained in ten seconds</h4>
  <div class="img" role="img" aria-label="Lecturer standing in front of a chalkboard" style="background:linear-gradient(120deg,#5a6257,#8b9186 50%,#3e433e)"></div>
  <div class="text">
    <p><strong>Workplace Wire Headline News: Find out what's going on in the world of corporate and business communications.</strong> Signal Lines: Learn about using communications to better communicate within your organization, and with others outside your organization. Office Lens: This blog is meant for corporate communications professionals.</p>
    <p>Workplace Wire Headline News: Find out what's going on in the world of corporate and business communications.</p>
    <p><strong>Workplace Wire Headline News: Find out what's going on in the world of corporate and business communications.</strong> Signal Lines: Learn about using communications to better communicate within your organization, and with others outside your organization. Office Lens: This blog is meant for corporate communications professionals.</p>
  </div>
  <div class="more" style="top:177px;left:174px">Continue Reading</div>
  <div class="share" style="top:175px">Share This <i></i><i></i><i></i><i></i></div>
  <div class="rule" style="top:196px"></div>
</article>

<aside class="abs box connect">
  <h5>CONNECT WITH US:</h5>
  <span class="soc" style="left:11px;background:#3b5b98" role="img" aria-label="Social link"></span>
  <span class="soc" style="left:43px;background:var(--orange)" role="img" aria-label="Feed link"></span>
  <span class="soc" style="left:75px;background:#3aa1dd" role="img" aria-label="Social link"></span>
  <span class="soc" style="left:108px;background:#d33b30" role="img" aria-label="Video channel link"></span>
</aside>

<aside class="abs box helpful">
  <div class="side-title" style="top:10px">Helpful Resources</div>
  <ul>
    <li>Kestrel Tuts</li>
    <li>Loom Docs</li>
    <li>Gadgetry Docs</li>
    <li>Menagerie Docs</li>
    <li>Menagerie Download</li>
    <li>Social Icons Download</li>
    <li style="border:0">Menu Icons Download</li>
  </ul>
  <div class="access">GET INSTANT ACCESS NOW</div>
</aside>

<aside class="abs box lastest">
  <div class="side-title" style="top:10px">Lastest Post</div>
  <div class="lp" style="top:32px">
    <a>Xeno Rift v1.5.1 Droidline Game Full APK Free Download</a>
    <div class="thumb" role="img" aria-label="Game artwork thumbnail"></div>
    <p>Xeno Rift v1.5.1 Droidline Game Requires GripPad controller suppor issue...</p>
  </div>
  <div class="lp" style="top:115px">
    <a>Xeno Rift v1.5.1 Droidline Game Full APK Free Download</a>
    <div class="thumb" role="img" aria-label="Game artwork thumbnail"></div>
    <p>Xeno Rift v1.5.1 Droidline Game Requires GripPad controller suppor issue...</p>
  </div>
</aside>

<aside class="abs box tags">
  <span class="tag-icon"></span>
  <h5>TAGS</h5>
  <div class="cloud">
    <div><span style="font-size:18px">Negotiate</span> <span style="font-size:8px">Pricing</span></div>
    <div><span style="font-size:8.5px">Banking fees</span> &nbsp;<span style="font-size:12px">Tricks Tips</span></div>
    <div><span style="font-size:13px">Best Treasury Advisors</span></div>
    <div><span style="font-size:8.5px">Earnings Credit Rates</span> <span style="font-size:12px">Tools</span></div>
    <div><span style="font-size:13px">Service Definitions</span></div>
    <div><span style="font-size:11px">Treasury Consultant</span></div>
    <div style="margin-top:7px"><span style="font-size:9px">Referrals</span> <span style="font-size:18px">Consulting</span></div>
  </div>
</aside>

<footer class="abs footer">
  <div class="fcol" style="left:78px"><h6>CATEGORIES</h6><ul><li>Did You Know?</li><li>Treasury Fundamentals</li><li>60 Second Lessons</li><li>Recommend</li><li>About</li></ul></div>
  <div class="fcol" style="left:210px"><h6>POLICIES</h6><ul><li>Privacy Policy</li><li>Affiliate Disclaimer</li><li>Copyright</li><li>External Link Policy</li><li>Anti Spam Policy</li><li>DCMA Disclaimer</li></ul></div>
  <div class="fcol addr" style="left:336px"><h6>ADDRESS</h6><ul><li>418 Halden Row</li><li>Suite 12</li><li>Marrowfield, NC 27990</li></ul></div>
</footer>
<div class="abs map" role="img" aria-label="Street map of the office location"></div>
<div class="abs bottom">
  <nav><span>Home</span><span>About us</span><span>The team</span><span>Resume tips</span><span>Timesheets</span><span>Send resume</span><span>Candidates</span><span>Location</span><span>Contact us</span></nav>
  <p>© 2012 zetaquarks.org - The Hiring Desk</p>
</div>
</body>
</html>
```